Stellenanzeige Mechaniker für Baumaschinen
Zielgruppe
Was wir machen: Baumaschinenhandel und Vermietung
Was wir suchen: Vollzeitkräfte in der Werkstatt Service und Verkauf
www.baumaschinen-krosbach.de
www.krosbach-rental.de
Aufgabenstellung
Eyecatcher, die Anzeige soll in diversen Medien gestreut werden.
Ihr Aufgabengebiet
Zuverlässig umsetzen: Sie reparieren Neu- und Gebrauchtmaschinen im Außen- und Innendienst
Sicherheit schaffen: Durchführung von Inspektionen, UVV-Prüfungen und Wartungsarbeiten
Probleme beseitigen: Fehler- und Störungsanalyse
Werte entdecken: Aufarbeitung von Gebraucht- und Mietmaschinen
Kundenzufriedenheit garantieren: Aus- und Umrüsten vom Maschinen mit Zubehör Kundenbetreuung im Servicebereich sowie Ersatzteilbeschaffung und Garantieabwicklungen
Ihr Profil
Ausbildung: als Land-/Baumaschinenmechaniker oder vergleichbare Ausbildung
Persönlichkeit: kommunikatives und sympathisches Auftreten, hohes Qualitätsbewusstsein,
Arbeitsweise: selbständig, strukturiert, belastbar und zuverlässig
Erfahrungen und Knowhow: Einschlägige Berufserfahrung in der Branche, Sichere PC-Anwendung (Diagnose-Tools), Gute Kenntnisse in Hydraulik, Elektrik und Motoren
Mobilität: Führerschein Klasse B (Pkw)
Wir bieten:
Zukunfts- und krisensicherer Arbeitsplatz
Interessante und abwechslungsreiche Aufgaben in einer vertrauensvollen Arbeitsatmosphäre
Attraktive Vergütung
Fundierte und strukturierte Einarbeitung
Weiterbildungs- und Entwicklungsmöglichkeiten
Gutes Betriebsklima in einer familiären Atmosphäre
Kurze Entscheidungswege

```html
<!DOCTYPE html>
<html lang="en">
<head>
<meta charset="utf-8">
<title>Krosbach Baumaschinen – Job Ad</title>
<link rel="stylesheet" href="https://fonts.googleapis.com/css2?family=Montserrat:wght@500;700;800;900&family=Oswald:wght@500&family=Yellowtail&display=swap">
<style>
  :root{
    --teal:#2aa5a6;
    --teal-dark:#1f8e8f;
    --yellow:#ffd400;
    --navy:#15267c;
    --ink:#111111;
    --white:#ffffff;
    --grey:#e7e7e7;
  }
  *{margin:0;padding:0;box-sizing:border-box}
  html,body{width:1200px;height:1200px;overflow:hidden;background:var(--white)}
  .ad{position:relative;width:1200px;height:1200px;overflow:hidden;font-family:"Montserrat",Arial,sans-serif}
  .ad-shapes{position:absolute;inset:0;width:1200px;height:1200px}
  .abs{position:absolute}

  .brand{left:72px;top:72px;display:flex;align-items:center;gap:14px}
  .brand-square{width:66px;height:66px;background:var(--yellow);border-radius:8px}
  .brand-name{font-weight:800;color:var(--ink);line-height:1}
  .brand-name .main{display:block;font-size:42px;letter-spacing:1px}
  .brand-name .sub{display:block;font-size:17px;letter-spacing:5.5px;margin-top:4px}

  .headline{left:76px;top:192px;font-weight:900;color:var(--yellow);font-size:70px;line-height:88px;text-shadow:0 3px 6px rgba(0,0,0,.25)}
  .subline{left:78px;top:358px;font-weight:800;font-size:39px;color:var(--white)}
  .subline .dark{color:var(--ink)}
  .service-bar{left:70px;top:412px;width:472px;height:48px;background:var(--yellow);font-weight:800;font-size:39px;line-height:48px;color:var(--ink);padding-left:8px}
  .service-bar .light{color:var(--white)}

  .apply{left:74px;top:520px;width:296px;height:70px;border-radius:35px;background:var(--yellow);color:var(--navy);font-weight:800;font-size:30px;line-height:70px;text-align:center}
  .apply::before{content:"";position:absolute;left:38px;top:-20px;border-left:14px solid transparent;border-right:14px solid transparent;border-bottom:22px solid var(--yellow)}

  .offer-title{left:82px;top:636px;font-family:"Yellowtail",cursive;font-weight:400;font-size:48px;letter-spacing:2px;color:var(--white)}
  .offer-list{left:76px;top:721px;list-style:none}
  .offer-list li{display:table;background:var(--yellow);color:var(--ink);font-family:"Oswald",Arial,sans-serif;font-weight:500;font-size:14px;letter-spacing:1px;text-transform:uppercase;height:24px;line-height:24px;padding:0 5px;margin-bottom:11.5px}

  .hiring{left:636px;top:42px;width:300px;height:300px;border-radius:50%;display:flex;flex-direction:column;align-items:center;justify-content:center;text-align:center}
  .hiring .title{color:var(--yellow);font-weight:800;font-size:25px;margin-bottom:12px}
  .hiring .line{color:var(--white);font-weight:500;font-size:21px;line-height:44px;letter-spacing:.5px}

  .contact-phone{left:58px;top:1012px;display:flex;align-items:center;gap:12px}
  .phone-icon{width:28px;height:42px}
  .phone-number{font-weight:800;font-size:30px;color:var(--ink)}
  .contact-web{left:107px;top:1056px;font-weight:500;font-size:15.5px;line-height:22px;color:#333}
  .partner{left:72px;top:1120px;font-weight:900;font-size:46px;letter-spacing:1px;color:var(--teal)}
</style>
</head>
<body>
<main class="ad">
  <svg class="ad-shapes" viewBox="0 0 1080 1080">
    <defs>
      <linearGradient id="site-photo" x1="0.15" y1="0" x2="0.35" y2="1">
        <stop offset="0" stop-color="#f1dccb"/>
        <stop offset="0.18" stop-color="#d8c3b6"/>
        <stop offset="0.3" stop-color="#3fb8bc"/>
        <stop offset="0.45" stop-color="#2fb0b4"/>
        <stop offset="0.55" stop-color="#c98a5a"/>
        <stop offset="0.68" stop-color="#5a4a44"/>
        <stop offset="0.85" stop-color="#2e2b2c"/>
        <stop offset="1" stop-color="#4a3a33"/>
      </linearGradient>
      <linearGradient id="mechanic-photo" x1="0" y1="0" x2="1" y2="1">
        <stop offset="0" stop-color="#d8d8d8"/>
        <stop offset="0.3" stop-color="#d9e85a"/>
        <stop offset="0.55" stop-color="#2f4c7a"/>
        <stop offset="0.8" stop-color="#2aa5a6"/>
        <stop offset="1" stop-color="#1c2333"/>
      </linearGradient>
      <linearGradient id="fleet-photo" x1="0" y1="0" x2="0" y2="1">
        <stop offset="0" stop-color="#a9b0b6"/>
        <stop offset="0.4" stop-color="#35aeb2"/>
        <stop offset="0.7" stop-color="#2a8f93"/>
        <stop offset="1" stop-color="#24272b"/>
      </linearGradient>
    </defs>

    <path class="bg-grey" d="M0 860 H260 Q300 860 330 890 L520 1080 H0 Z" fill="var(--grey)"/>
    <path class="bg-teal" d="M0 0 H780 L1000 220 Q1020 250 995 275 L480 790 Q450 820 420 790 L330 720 L0 900 Z" fill="var(--teal)"/>

    <g role="img" aria-label="Photo: mechanic in hard hat and hi-vis vest servicing a teal excavator on a construction site">
      <path d="M250 560 L660 150 L1080 150 L1080 640 L640 1000 Q610 1020 580 990 Z" fill="url(#site-photo)" stroke="url(#site-photo)" stroke-width="20" stroke-linejoin="round"/>
    </g>

    <path class="tab-teal" d="M600 0 H800 L985 185 Q1010 215 985 245 L925 305 L640 305 Z" fill="var(--teal)"/>
    <path class="tab-yellow" d="M745 0 H830 L925 95 Q945 120 920 140 Z" fill="var(--yellow)"/>

    <circle cx="705" cy="170" r="146" fill="var(--white)"/>
    <circle cx="705" cy="170" r="139" fill="var(--navy)"/>

    <g role="img" aria-label="Photo: mechanic in red hard hat working on an engine compartment">
      <rect x="825" y="730" width="150" height="150" rx="22" transform="rotate(45 900 805)" fill="url(#mechanic-photo)" stroke="var(--yellow)" stroke-width="7"/>
    </g>
    <g role="img" aria-label="Photo: row of new teal mini excavators">
      <rect x="595" y="905" width="190" height="190" rx="24" transform="rotate(45 690 1000)" fill="url(#fleet-photo)" stroke="var(--yellow)" stroke-width="7"/>
    </g>
  </svg>

  <div class="abs brand">
    <span class="brand-square"></span>
    <span class="brand-name"><span class="main">KROSBACH</span><span class="sub">BAUMASCHINEN</span></span>
  </div>

  <h1 class="abs headline">FULL-TIME<br>EMPLOYEES</h1>
  <p class="abs subline">IN THE <span class="dark">WORKSHOP</span></p>
  <p class="abs service-bar">SERVICE <span class="light">AND</span> SALES</p>

  <div class="abs apply">APPLY NOW</div>

  <div class="abs hiring">
    <p class="title">WE’RE HIRING!</p>
    <p class="line">“ REPAIR NEW</p>
    <p class="line">AND USED MACHINES</p>
    <p class="line">IN THE FIELD</p>
    <p class="line">AND OFFICE ”</p>
  </div>

  <h2 class="abs offer-title">We Offer:</h2>
  <ul class="abs offer-list">
    <li>Future-proof and crisis-proof workplace</li>
    <li>Interesting and varied tasks in a trusting working atmosphere</li>
    <li>Attractive remuneration</li>
    <li>Well-founded and structured induction</li>
    <li>Training and development opportunities</li>
    <li>Good working atmosphere in a familiar atmosphere</li>
    <li>Short decision-making paths</li>
  </ul>

  <div class="abs contact-phone">
    <svg class="phone-icon" viewBox="0 0 28 42" aria-hidden="true">
      <path d="M10 2 H4 Q2 2 2 6 V36 Q2 40 4 40 H10 L10 30 H7 V12 H10 Z" fill="none" stroke="var(--ink)" stroke-width="2.5" stroke-linejoin="round"/>
    </svg>
    <span class="phone-number">+06000 - 4817302</span>
  </div>
  <p class="abs contact-web">www.baumaschinen-krosbach.de<br>www.krosbach-rental.de</p>

  <p class="abs partner">STELLVANE</p>
</main>
</body>
</html>
```